Graphic to hang inside of fitness studio

This graphic will be printed on vinyl and hung inside of a boutique fitness studio for 2019. Graphic should read YEAR OF POSSIBILITIES.

2018 was called Year of Living Well. We would like something on trend for 2019 to hang within the studio as our 2019 Mantra. It is not a logo but for internal use. I've attached our logo here and the website is www.kestrelmovehall.com for additional reference. Thank you.

Target Market(s)

25 to 45 women

Industry/Entity Type

Fitness

Colors

Designer to choose colors to be used in the design.

Requirements
Must have
• On trend for 2019. (no people in image)
• Year of Possibilities in trendy font.
• Easy to read.
• Need text only.
• Do not need graphic images.
Nice to have
• Tintorell colours for 2019
• 2019 design trends for background
Should not have
• Male dominate colour or masculine traits.
• Photos of fitness.
• Photos of people.
• Photos of equipment.

```html
<!DOCTYPE html>
<html lang="en">
<head>
<meta charset="utf-8">
<title>Year of Possibilities</title>
<link href="https://fonts.googleapis.com/css2?family=Marcellus&display=swap" rel="stylesheet">
<style>
  :root {
    --canvas-bg: #ffffff;
    --band-cream: #fbf3e2;
    --text-white: #ffffff;
    --text-soft: rgba(255, 255, 255, 0.78);
  }
  html, body {
    margin: 0;
    padding: 0;
    width: 1200px;
    height: 761px;
    overflow: hidden;
    background: var(--canvas-bg);
  }
  .mantra-poster {
    display: block;
    width: 1200px;
    height: 761px;
  }
  .separator-band {
    fill: none;
    stroke: var(--band-cream);
    stroke-width: 20;
    stroke-opacity: 0.82;
  }
  .separator-glow {
    fill: none;
    stroke: #f3a03a;
    stroke-width: 34;
    stroke-opacity: 0.35;
  }
  .mantra-text {
    font-family: "Marcellus", "Optima", serif;
    font-size: 64px;
    letter-spacing: 3px;
  }
  .mantra-lead { fill: var(--text-soft); }
  .mantra-main { fill: var(--text-white); }
  .mantra-tail {
    fill: var(--text-white);
    letter-spacing: 9px;
  }
</style>
</head>
<body>
<svg class="mantra-poster" viewBox="0 0 1200 761" xmlns="http://www.w3.org/2000/svg">
  <defs>
    <linearGradient id="cliff-scene" x1="0" y1="0" x2="0" y2="1">
      <stop offset="0" stop-color="#e9e4d2"/>
      <stop offset="0.35" stop-color="#d7d2c2"/>
      <stop offset="0.55" stop-color="#9aa08c"/>
      <stop offset="0.75" stop-color="#4f5a44"/>
      <stop offset="0.88" stop-color="#8a5c44"/>
      <stop offset="1" stop-color="#6e4634"/>
    </linearGradient>
    <linearGradient id="statue-scene" x1="0" y1="0" x2="1" y2="1">
      <stop offset="0" stop-color="#b9a66a"/>
      <stop offset="0.4" stop-color="#7e6c4c"/>
      <stop offset="0.75" stop-color="#8d7a5a"/>
      <stop offset="1" stop-color="#5f7a3c"/>
    </linearGradient>
    <linearGradient id="forest-scene" x1="0" y1="0" x2="0" y2="1">
      <stop offset="0" stop-color="#d8641c"/>
      <stop offset="0.3" stop-color="#f2b53c"/>
      <stop offset="0.55" stop-color="#e9c24a"/>
      <stop offset="0.8" stop-color="#e0761e"/>
      <stop offset="1" stop-color="#c2461a"/>
    </linearGradient>
    <radialGradient id="lotus-scene" cx="0.55" cy="0.4" r="0.7">
      <stop offset="0" stop-color="#efd6e8"/>
      <stop offset="0.45" stop-color="#d69ccd"/>
      <stop offset="0.8" stop-color="#b27ab4"/>
      <stop offset="1" stop-color="#3b3936"/>
    </radialGradient>
  </defs>

  <rect class="panel panel-lotus" x="0" y="0" width="1200" height="761" fill="url(#lotus-scene)"
        role="img" aria-label="Close-up photograph of a pink lotus flower"/>
  <path class="panel panel-forest" fill="url(#forest-scene)"
        d="M0,0 L985,0 C900,120 865,250 865,380 C865,520 960,640 1000,761 L0,761 Z"
        role="img" aria-label="Sunlit autumn forest with a silhouette in a standing balance pose"/>
  <path class="panel panel-statue" fill="url(#statue-scene)"
        d="M0,0 L660,0 C620,160 495,300 495,390 C495,470 640,600 690,761 L0,761 Z"
        role="img" aria-label="Soft-focus carved wooden statue with green leaves"/>
  <path class="panel panel-cliff" fill="url(#cliff-scene)"
        d="M0,0 L385,0 C300,150 215,280 215,400 C215,520 330,640 420,761 L0,761 Z"
        role="img" aria-label="Woman in tree pose on a rocky cliff above a misty valley"/>

  <g class="separators">
    <path class="separator-glow" d="M385,0 C300,150 215,280 215,400 C215,520 330,640 420,761"/>
    <path class="separator-band" d="M385,0 C300,150 215,280 215,400 C215,520 330,640 420,761"/>
    <path class="separator-band" d="M660,0 C620,160 495,300 495,390 C495,470 640,600 690,761"/>
    <path class="separator-band" d="M985,0 C900,120 865,250 865,380 C865,520 960,640 1000,761"/>
  </g>

  <text class="mantra-text" x="360" y="723">
    <tspan class="mantra-lead">YEAR OF </tspan><tspan class="mantra-main">POSSIBILI</tspan>
  </text>
  <text class="mantra-text mantra-tail" transform="translate(1156,723) rotate(-90)" x="0" y="0">TIES</text>
</svg>
</body>
</html>
```